Support People to improve their image and well-being by provided personalised advise

We need a design for business cards that could be used for production on plato press. We build a new business in our region for advising mostly women (also men though) on style embracing several aspects including fashion, style, self-confidence and ultimately your internal and external image. The business card should be "classy", "french-style". The business is located in the french -speaking part of Switzerland, close to France. The name of the company is Velo Grace

Target Market(s)

Service fees won't be cheap (medium to premium) thus we target mid-class to upper-class women (1st target) and men (2nd target)

Industry/Entity Type

Life Coaching

Contact Information for Business Card

Conseil en Image

+41 79 418 62 07
morinetu@velo-grace.ch
linkedin.com/in/tu-moro-netia

Logo Text

Velo Grace

Colors

Designer to choose colors to be used in the design.

```html
<!DOCTYPE html>
<html lang="fr">
<head>
<meta charset="utf-8">
<title>Velo Grace — Cartes de visite</title>
<link rel="stylesheet" href="https://fonts.googleapis.com/css2?family=Tinos&display=swap">
<style>
  :root {
    --page: #ffffff;
    --card: #201f20;
    --brand-purple: #6b4f8e;
    --band-purple: #3f3660;
    --ink-light: #ffffff;
  }
  html, body {
    margin: 0;
    padding: 0;
    width: 1200px;
    height: 1200px;
    overflow: hidden;
    background: var(--page);
    font-family: "Tinos", "Times New Roman", serif;
  }
  .canvas {
    position: relative;
    width: 1200px;
    height: 1200px;
  }
  .card {
    position: absolute;
    left: 115px;
    width: 970px;
    height: 557px;
    background: var(--card);
    overflow: hidden;
  }
  .card--front { top: 30px; }
  .card--back { top: 613px; }

  /* Front */
  .front-mark {
    position: absolute;
    left: 0;
    right: 0;
    top: 130px;
    text-align: center;
  }
  .front-mark__dot {
    display: inline-block;
    width: 64px;
    height: 64px;
    border-radius: 50%;
    background: var(--brand-purple);
  }
  .front-mark__name {
    display: block;
    margin-top: 40px;
    color: var(--brand-purple);
    font-size: 78px;
    line-height: 1;
  }
  .front-band {
    position: absolute;
    left: 0;
    top: 469px;
    width: 970px;
    height: 88px;
    display: block;
  }

  /* Back */
  .back-mark {
    position: absolute;
    left: 0;
    width: 429px;
    top: 225px;
    text-align: center;
  }
  .back-mark__dot {
    display: inline-block;
    width: 46px;
    height: 46px;
    border-radius: 50%;
    background: var(--ink-light);
  }
  .back-mark__name {
    display: block;
    margin-top: 26px;
    color: var(--ink-light);
    font-size: 52px;
    line-height: 1;
  }
  .divider {
    position: absolute;
    left: 428px;
    top: 92px;
    width: 3px;
    height: 373px;
    background: var(--ink-light);
  }
  .details {
    position: absolute;
    left: 480px;
    top: 0;
    color: var(--ink-light);
  }
  .details__service {
    position: absolute;
    top: 86px;
    margin: 0;
    font-size: 43px;
    font-weight: 400;
    white-space: nowrap;
  }
  .details__phone,
  .details__email,
  .details__social {
    position: absolute;
    margin: 0;
    white-space: nowrap;
  }
  .details__phone { top: 342px; font-size: 37px; }
  .details__email { top: 390px; font-size: 28px; }
  .details__social { top: 434px; font-size: 28px; }
</style>
</head>
<body>
<main class="canvas">
  <section class="card card--front" aria-label="Recto">
    <div class="front-mark">
      <span class="front-mark__dot"></span>
      <span class="front-mark__name">Velo Grace</span>
    </div>
    <svg class="front-band" viewBox="0 0 970 88" aria-hidden="true">
      <polygon points="0,0 434,0 485,27 536,0 970,0 970,88 0,88" fill="var(--band-purple)"/>
    </svg>
  </section>

  <section class="card card--back" aria-label="Verso">
    <div class="back-mark">
      <span class="back-mark__dot"></span>
      <span class="back-mark__name">Velo Grace</span>
    </div>
    <div class="divider"></div>
    <div class="details">
      <h2 class="details__service">Conseil en Image</h2>
      <p class="details__phone">+41 79 418 62 07</p>
      <p class="details__email">morinetu@velo-grace.ch</p>
      <p class="details__social">linkedin.com/in/tu-moro-netia</p>
    </div>
  </section>
</main>
</body>
</html>
```